Halvard 7 Rower Vinyl Designs and Halvard Vinyl TrekVane Designs

We would like to have a great design for our Rowers and TrekVanes. The background of the stickers should be dark. Fade or structure is possible. Use our CI Booklet for Fonts, Colors and Logo.

```html
<!DOCTYPE html>
<html lang="en">
<head>
<meta charset="utf-8">
<title>Halvard 7 Rower &amp; TrekVane Vinyl Strips</title>
<link href="https://fonts.googleapis.com/css2?family=Inter:wght@400;700;900&display=swap" rel="stylesheet">
<style>
  :root {
    --page: #ffffff;
    --ink-black: #0a0b0d;
    --ink-navy: #111b2a;
    --glow-blue: #1b4d7e;
    --brand-blue: #163f66;
    --text-white: #f2f3f5;
    --text-grey: #808080;
  }
  html, body {
    margin: 0;
    padding: 0;
    width: 1200px;
    height: 3784px;
    overflow: hidden;
    background: var(--page);
    font-family: "Inter", Arial, sans-serif;
  }
  .canvas {
    position: relative;
    width: 1200px;
    height: 3784px;
  }
  .strip {
    position: absolute;
    top: 202px;
    width: 174px;
    height: 3320px;
    display: flex;
    flex-direction: column;
    align-items: center;
    overflow: hidden;
  }
  .strip--rower {
    left: 345px;
    background:
      radial-gradient(circle at 100% 0%, var(--glow-blue) 0, transparent 180px),
      radial-gradient(circle at 0% 100%, var(--glow-blue) 0, transparent 180px),
      var(--ink-black);
  }
  .strip--trekvane {
    left: 664px;
    background:
      radial-gradient(circle at 100% 0%, var(--glow-blue) 0, transparent 180px),
      radial-gradient(circle at 0% 100%, var(--glow-blue) 0, transparent 180px),
      var(--ink-navy);
  }
  .brand {
    position: absolute;
    top: 684px;
    display: flex;
    flex-direction: column;
    align-items: center;
    gap: 26px;
  }
  .brand__dot {
    width: 86px;
    height: 86px;
    border-radius: 50%;
    background: var(--brand-blue);
  }
  .brand__name {
    writing-mode: vertical-rl;
    font-weight: 700;
    font-size: 46px;
    letter-spacing: 2px;
    color: var(--text-white);
    line-height: 1;
  }
  .divider {
    position: absolute;
    top: 1198px;
    width: 90px;
    height: 13px;
    background: var(--brand-blue);
  }
  .slogan {
    position: absolute;
    top: 1405px;
    writing-mode: vertical-rl;
    font-size: 122px;
    line-height: 1;
    white-space: nowrap;
    text-shadow: 0 6px 18px rgba(0,0,0,0.5);
  }
  .slogan__lead { font-weight: 700; color: var(--text-white); }
  .slogan__mid { font-weight: 400; color: var(--text-grey); }
  .slogan__key { font-weight: 900; color: var(--brand-blue); }
</style>
</head>
<body>
<div class="canvas">
  <section class="strip strip--rower" aria-label="Halvard 7 rower vinyl strip">
    <div class="brand">
      <div class="brand__dot"></div>
      <div class="brand__name">VALDMARK</div>
    </div>
    <div class="divider"></div>
    <p class="slogan"><span class="slogan__lead">EARN</span> <span class="slogan__mid">YOUR</span> <span class="slogan__key">METERS</span></p>
  </section>

  <section class="strip strip--trekvane" aria-label="Halvard TrekVane vinyl strip">
    <div class="brand">
      <div class="brand__dot"></div>
      <div class="brand__name">VALDMARK</div>
    </div>
    <div class="divider"></div>
    <p class="slogan"><span class="slogan__lead">PULL</span> <span class="slogan__mid">WITH</span> <span class="slogan__key">POWER</span></p>
  </section>
</div>
</body>
</html>
```